TALMORK

The business want a professional looking business card. We have a scetch we will add but want the extra upgrade, and would like more suggestions for variations of our business cards.

```html
<!DOCTYPE html>
<html lang="en">
<head>
<meta charset="UTF-8">
<title>TALMORK Business Cards</title>
<link href="https://fonts.googleapis.com/css2?family=Poppins:wght@400;500&family=Playfair+Display:wght@500&display=swap" rel="stylesheet">
<style>
  :root {
    --backdrop: #2b2b2d;
    --card: #222223;
    --gold: #d4a93c;
    --gold-soft: #c99d35;
    --mark-faint: #2b2a27;
    --mark-gloss: #151516;
  }
  * { box-sizing: border-box; margin: 0; padding: 0; }
  html, body {
    width: 1200px; height: 900px; overflow: hidden;
    background: var(--backdrop);
    font-family: "Poppins", sans-serif;
  }
  .canvas { position: relative; width: 1200px; height: 900px; }
  .card {
    position: absolute;
    width: 620px; height: 354px;
    background: var(--card);
    border-radius: 22px;
    box-shadow: 0 18px 40px rgba(0,0,0,.45);
    overflow: hidden;
  }
  .card--back { left: 500px; top: 60px; }
  .card--front { left: 80px; top: 480px; }

  .brand { display: flex; align-items: center; gap: 14px; position: absolute; }
  .brand__dot { width: 40px; height: 40px; border-radius: 50%; background: var(--gold); }
  .brand__block { display: flex; flex-direction: column; align-items: center; }
  .brand__name {
    font-weight: 500; color: var(--gold);
    font-size: 40px; letter-spacing: 10px; line-height: 1;
  }
  .brand__since {
    font-size: 12px; letter-spacing: 5px; color: var(--gold);
    margin-top: 6px;
  }
  .card--back .brand { right: 40px; bottom: 46px; }
  .card--back .brand__name { font-size: 34px; letter-spacing: 9px; }
  .card--front .brand { left: 46px; top: 48px; }

  .decor { position: absolute; border-radius: 50%; }
  .card--back .decor { left: 70px; top: -20px; width: 330px; height: 330px; background: radial-gradient(circle at 65% 55%, #3a3a3c, var(--mark-gloss) 70%); }
  .card--front .decor { right: -40px; bottom: -60px; width: 300px; height: 300px; background: var(--mark-faint); }

  .contact { position: absolute; left: 50px; top: 168px; color: var(--gold); }
  .contact__name { font-family: "Playfair Display", serif; font-size: 26px; font-weight: 500; }
  .contact__role, .contact__person { font-size: 15px; color: var(--gold-soft); line-height: 1.45; }
  .contact__list { list-style: none; margin-top: 14px; }
  .contact__list li { display: flex; align-items: center; gap: 10px; font-size: 15px; line-height: 1.6; }
  .contact__list svg { width: 14px; height: 14px; fill: var(--gold); flex: none; }
</style>
</head>
<body>
<main class="canvas">
  <section class="card card--back">
    <div class="decor" role="img" aria-label="Large glossy brand mark decoration"></div>
    <div class="brand">
      <div class="brand__block">
        <span class="brand__name">TALMORK</span>
        <span class="brand__since">SINCE 2026</span>
      </div>
    </div>
  </section>

  <section class="card card--front">
    <div class="decor" role="img" aria-label="Faint brand mark decoration"></div>
    <div class="brand">
      <span class="brand__dot"></span>
      <div class="brand__block">
        <span class="brand__name">TALMORK</span>
        <span class="brand__since">SINCE 2026</span>
      </div>
    </div>
    <div class="contact">
      <h1 class="contact__name">Talmork Vestli</h1>
      <p class="contact__role">CEO &amp; Founder</p>
      <p class="contact__person">Erik Solberg Haugen</p>
      <ul class="contact__list">
        <li><svg viewBox="0 0 16 16"><path d="M3 1h3l1.5 4-2 1.5a9 9 0 0 0 4 4L11 8.5l4 1.5v3c0 1-1 2-2 2A12 12 0 0 1 1 3c0-1 1-2 2-2z"/></svg>004791234567</li>
        <li><svg viewBox="0 0 16 16"><path d="M1 3h14v10H1z M1 3l7 6 7-6" fill="none" stroke="#d4a93c" stroke-width="1.6"/></svg>talmork.llc@postmail.net</li>
        <li><svg viewBox="0 0 16 16"><circle cx="8" cy="8" r="6.5" fill="none" stroke="#d4a93c" stroke-width="1.5"/><path d="M1.5 8h13M8 1.5c-3 3.5-3 9.5 0 13M8 1.5c3 3.5 3 9.5 0 13" fill="none" stroke="#d4a93c" stroke-width="1.2"/></svg>www.talmork.llc</li>
      </ul>
    </div>
  </section>
</main>
</body>
</html>
```